Creative, fun banner ads needed for tropical shaved ice company

Create assorted, most popular-sized banner ads for shaved ice company> Logo files attached. Looking for eye-catching, fun ads that would make any parent of a child 2-17 years old want to click the ad and have us to be a part of the festivities so they can enjoy our tropical-flavored shaved ice; to hire us for a party or community event or fund-raiser.

Target Market(s)

parents with children between 2 - 18 years of age; charities, fund-raisers, event planners. think about the websites/CL pages where this ad will most like appear.

Font styles to use
Sans Serif

Requirements
Must have
• 1. logo
2. must be editable so I can reuse for different themes (birthdays, major holidays, special events, charity events)
3. colorful or otherwise eye-catching/appealing.
4. keep with the logo theme OR use logo and have different, yet fun, happy theme
5. otherwise simple, clean, pleasant design that illicits a fun, happy image
6. just keep in mind that shaved ice is delicious, fun, and beats the scorching sun here in South Florida. https://palmcovesnowcones.com or https://chatterlink.com/palmcovesnowcones
Nice to have
• reuse iguana character somehow; possibly holding a shaved ice
lighthouse
Should not have
• dark or gloomy colors/themes
too much stuff; too much clutter.

```html
<!DOCTYPE html>
<html lang="en">
<head>
<meta charset="utf-8">
<title>Palm Cove Snow Cones – Perfectly shaved</title>
<link href="https://fonts.googleapis.com/css2?family=Open+Sans:wght@600;700&display=swap" rel="stylesheet">
<style>
  :root {
    --green-light: #5cb150;
    --green-mid: #4ea34a;
    --green-dark: #3b8c45;
    --leaf-green: #2f7d3c;
    --white: #ffffff;
    --brand-green: #3f9a46;
    --treat-pink: #f2b6c8;
    --treat-blue: #8fc9ea;
    --treat-red: #e2455a;
  }
  * { margin: 0; padding: 0; box-sizing: border-box; }
  html, body { width: 1200px; height: 309px; overflow: hidden; background: var(--white); }
  .banner {
    position: relative;
    width: 1200px;
    height: 309px;
    overflow: hidden;
    background: linear-gradient(180deg, var(--green-light) 0%, var(--green-mid) 55%, var(--green-dark) 100%);
    font-family: "Open Sans", Arial, sans-serif;
    color: var(--white);
  }
  .shapes { position: absolute; inset: 0; }
  .leaf-art { position: absolute; }
  .leaf-art--left { left: 40px; top: 205px; width: 150px; height: 120px; }
  .leaf-art--center { left: 560px; top: 200px; width: 170px; height: 120px; }
  .treat-photo {
    position: absolute;
    left: 840px; top: 0;
    width: 360px; height: 309px;
  }
  .brand {
    position: absolute;
    left: 30px; top: 22px;
    width: 170px;
    display: flex; align-items: center; gap: 8px;
    text-decoration: none;
  }
  .brand__dot {
    flex: none;
    width: 22px; height: 22px;
    border-radius: 50%;
    background: var(--brand-green);
  }
  .brand__name {
    font-weight: 700;
    font-size: 20px;
    line-height: 1.15;
    color: var(--brand-green);
  }
  .headline {
    position: absolute;
    left: 317px; top: 20px;
    font-weight: 600;
    font-size: 64px;
    line-height: 1;
    letter-spacing: -0.5px;
  }
  .body-copy {
    position: absolute;
    left: 319px; top: 112px;
    width: 510px;
    font-weight: 700;
    font-size: 17.5px;
    line-height: 27px;
  }
  .social {
    position: absolute;
    left: 305px; top: 272px;
    display: flex; gap: 20px;
    list-style: none;
  }
  .social a {
    display: block;
    font-weight: 700;
    font-size: 13px;
    color: var(--brand-green);
    text-decoration: none;
  }
</style>
</head>
<body>
<div class="banner">
  <svg class="shapes" width="1200" height="309" viewBox="0 0 1200 309" aria-hidden="true">
    <!-- top-left brand blob -->
    <path fill="#fff" d="M0 0 H310 C300 30 270 40 275 80 C280 120 250 150 215 155 C190 158 175 175 170 190 C160 215 120 215 105 195 C90 175 60 170 35 175 C15 178 0 170 0 160 Z"/>
    <circle fill="#fff" cx="215" cy="180" r="6"/>
    <circle fill="#fff" cx="232" cy="160" r="4"/>
    <!-- bottom social blob -->
    <path fill="#fff" d="M270 255 C262 235 285 225 305 232 C318 237 322 228 335 225 C350 222 352 240 372 238 C395 236 420 240 435 258 C448 275 440 295 425 309 H285 C275 295 280 275 270 255 Z"/>
    <circle fill="#fff" cx="330" cy="240" r="6"/>
    <circle fill="#fff" cx="352" cy="232" r="4"/>
    <!-- thin decorative curve -->
    <path fill="none" stroke="#fff" stroke-width="1.5" opacity="0.8" d="M440 309 C480 250 560 240 620 270 C680 300 740 280 760 255"/>
    <!-- right white blob behind treats -->
    <path fill="#fff" d="M1200 0 H885 C860 25 880 55 865 80 C845 110 815 125 830 165 C845 200 880 205 875 240 C870 275 900 309 940 309 H1200 Z"/>
  </svg>

  <div class="leaf-art leaf-art--left" role="img" aria-label="Faint tropical monstera leaf decoration"
       style="background: radial-gradient(ellipse at 50% 60%, rgba(47,125,60,0.55), rgba(47,125,60,0) 70%); border-radius: 50% 50% 40% 40%;"></div>
  <div class="leaf-art leaf-art--center" role="img" aria-label="Faint palm leaf decoration"
       style="background: radial-gradient(ellipse at 50% 55%, rgba(47,125,60,0.45), rgba(47,125,60,0) 70%); border-radius: 50%;"></div>

  <div class="treat-photo" role="img"
       aria-label="Photo of three rainbow, red and pink shaved ice cups with strawberry, blueberries and an orange slice"
       style="background: radial-gradient(circle at 30% 55%, var(--treat-blue) 0, rgba(143,201,234,0) 28%), radial-gradient(circle at 55% 45%, var(--treat-red) 0, rgba(226,69,90,0) 26%), radial-gradient(circle at 78% 55%, var(--treat-pink) 0, rgba(242,182,200,0) 30%); opacity: 0.9;"></div>

  <a class="brand" href="https://palmcovesnowcones.com">
    <span class="brand__dot"></span>
    <span class="brand__name">Palm Cove Snow Cones</span>
  </a>

  <h1 class="headline">Perfectly shaved</h1>
  <p class="body-copy">Quia dolor sit amet, consectetur, adipisci velit, sed quia non numquam eius modi tempora incidunt ut labore et dolore magnam aliquam quaerat voluptatem.</p>

  <ul class="social">
    <li><a href="https://chatterlink.com/palmcovesnowcones">CL</a></li>
    <li><a href="https://palmcovesnowcones.com">CH</a></li>
    <li><a href="https://palmcovesnowcones.com">SG</a></li>
  </ul>
</div>
</body>
</html>
```